Business Card Design Project

My business sells promotional merchandise to large blue chip companies. Gear like polo shirts, drink bottles, pens, basically anything that you can put a company logo onto.

I need the following elements included:
Logo as attached
Peter Hollingdale Managing Director
27 Corbel Street Tarrin Cove 4178
mobile 0438 514203
email kestrelpath@kestrelpathtrading.com.au

Promotional Merchandise with a difference

Target Market(s)

Mature age Marketing Managers

Industry/Entity Type

Business

```html
<!DOCTYPE html>
<html lang="en">
<head>
<meta charset="utf-8">
<title>Kestrel Path – Business Card</title>
<link rel="stylesheet" href="https://fonts.googleapis.com/css2?family=Josefin+Sans:wght@400&family=Saira+Semi+Condensed:wght@600&family=Tinos&family=Source+Sans+3:wght@400&display=swap">
<style>
  :root {
    --page-bg: #d9dadc;
    --card-deep: #08125a;
    --card-mid: #1233b8;
    --card-glow: #1f47d6;
    --ribbon: rgba(61, 71, 255, 0.55);
    --ribbon-fade: rgba(61, 71, 255, 0);
    --text-light: #ffffff;
    --accent-text: #5d6cff;
  }
  * { margin: 0; padding: 0; box-sizing: border-box; }
  html, body {
    width: 1200px;
    height: 900px;
    overflow: hidden;
    background: var(--page-bg);
  }
  .stage { position: relative; width: 1200px; height: 900px; }

  .card {
    position: absolute;
    overflow: hidden;
    background: radial-gradient(ellipse at 50% 55%, var(--card-glow) 0%, var(--card-mid) 35%, var(--card-deep) 100%);
    box-shadow: 0 6px 18px rgba(0,0,0,0.25);
  }
  .card-front { left: 90px; top: 30px; width: 790px; height: 460px; }
  .card-back  { left: 400px; top: 480px; width: 650px; height: 380px; }

  .ribbon-area {
    position: absolute;
    border-radius: 50%;
    background: radial-gradient(ellipse at center, var(--ribbon) 0%, var(--ribbon-fade) 70%);
  }
  .card-front .ribbon-area { left: 0; top: 70px; width: 790px; height: 280px; }
  .card-back .ribbon-top    { left: 10px; top: 20px; width: 310px; height: 120px; }
  .card-back .ribbon-bottom { left: 290px; top: 210px; width: 380px; height: 140px; }

  .brand-name {
    position: absolute;
    font-family: "Josefin Sans", sans-serif;
    font-weight: 400;
    color: var(--text-light);
    text-transform: uppercase;
    letter-spacing: 0.05em;
    white-space: nowrap;
    line-height: 1;
  }
  .card-front .brand-name { left: 220px; top: 210px; font-size: 52px; }
  .card-back .brand-name  { left: 42px; top: 190px; font-size: 40px; }

  .tagline {
    position: absolute;
    left: 112px; top: 292px;
    font-family: "Saira Semi Condensed", sans-serif;
    font-weight: 600;
    font-size: 27px;
    color: var(--text-light);
    white-space: nowrap;
  }

  .person {
    position: absolute;
    right: 28px; top: 365px;
    text-align: right;
    font-family: "Tinos", serif;
    line-height: 1.05;
  }
  .person-name { font-size: 26px; color: var(--text-light); }
  .person-role { font-size: 17px; color: var(--accent-text); letter-spacing: 0.08em; }

  .contact {
    position: absolute;
    left: 420px; top: 30px;
    padding-left: 8px;
    border-left: 1.5px solid var(--text-light);
    font-family: "Source Sans 3", sans-serif;
    font-style: normal;
    color: var(--text-light);
    line-height: 1.55;
  }
  .contact-name { font-size: 18px; }
  .contact-phone { font-size: 15px; }
  .contact-email, .contact-address { font-size: 13px; }
</style>
</head>
<body>
<main class="stage">

  <section class="card card-front" aria-label="Business card front">
    <div class="ribbon-area" role="img" aria-label="Flowing blue ribbon decoration"></div>
    <h1 class="brand-name">Kestrel Path</h1>
    <p class="tagline">"Promotional Merchandise with a difference"</p>
    <div class="person">
      <p class="person-name">PETER HOLLINGDALE</p>
      <p class="person-role">MANAGING DIRECTOR</p>
    </div>
  </section>

  <section class="card card-back" aria-label="Business card back">
    <div class="ribbon-area ribbon-top" role="img" aria-label="Flowing blue ribbon decoration"></div>
    <div class="ribbon-area ribbon-bottom" role="img" aria-label="Flowing blue ribbon decoration"></div>
    <address class="contact">
      <p class="contact-name">Peter Hollingdale</p>
      <p class="contact-phone">0438 514203</p>
      <p class="contact-email">kestrelpath@kestrelpathtrading.com.au</p>
      <p class="contact-address">27 Corbel Street Tarrin Cove 4178</p>
    </address>
    <p class="brand-name">Kestrel Path</p>
  </section>

</main>
</body>
</html>
```